Brochure for a website accessibility report

This brochure is related to a report that www.kelvat.org sell. The report shows the results of an automated audit of a websites accessibility. It shows details of issues found with screen shots, examples of code and provides remediation advice.

The brochure will be a pdf 8.5 inches by 11 inches. It can be anywhere from 6 to 10 pages.

The FaultLens™ name itself should be “Bree Serif” font. The fonts, styles, colors and sizes are up to you.

The images used and logo of the Office of Digital Openness and Q7N logo are upload

We highlighted in blue page extracts from the report we sell. Do not use the blue highlight, it is merely there to show you where the specific examples of the report we sell are vs the other content in the report. The areas in blue which show the content from the actual report should be shown as an extract of the actual page of the report. You have flexibility to change the layout and the way the content look.

The red square callouts over the blue content are callouts that describe the specific page extracts. We used it as a red callout only so that you would be able to see it. You should change the specific location, look and feel of the callout to be appropriate

Target Market(s)

Marketing and Technical people

Industry/Entity Type

Information Technology

Font styles to use
Sans Serif

Colors

Designer to choose colors to be used in the design.

Requirements
Should not have
• wheelchairs, images of blind people

```html
<!DOCTYPE html>
<html lang="en">
<head>
<meta charset="utf-8">
<title>FaultLens™ – Quick facts</title>
<link rel="stylesheet" href="https://fonts.googleapis.com/css2?family=Source+Sans+3:wght@400;700;900&display=swap">
<style>
  :root {
    --green: #2eae6b;
    --rule: #8fd3b0;
    --grey-band: #ececec;
    --ink: #231f20;
    --paper: #ffffff;
  }
  html, body { margin: 0; padding: 0; overflow: hidden; background: var(--paper); }
  .page {
    position: relative; width: 927px; height: 1200px; overflow: hidden;
    background: var(--paper); color: var(--ink);
    font-family: "Source Sans 3", Arial, sans-serif;
  }
  .side-band-top { position: absolute; left: 45px; top: 0; width: 135px; height: 393px; background: var(--grey-band); }
  .side-band-icons { position: absolute; left: 45px; top: 393px; width: 135px; height: 807px; background: var(--green); }
  .intro { position: absolute; left: 215px; top: 62px; width: 591px; }
  .product-name { font-size: 21px; font-weight: 700; margin: 0 0 12px; }
  .intro p { font-size: 13.6px; line-height: 17.5px; margin: 0 0 17px; text-align: justify; }
  .facts-title {
    position: absolute; left: 214px; top: 332px; margin: 0;
    font-size: 31px; font-weight: 900; color: var(--green); letter-spacing: -0.3px;
  }
  .fact { position: absolute; left: 215px; width: 495px; font-size: 13.6px; line-height: 17.5px; margin: 0; }
  .fact.wide { text-align: justify; hyphens: auto; }
  .fact-rule { position: absolute; left: 208px; width: 503px; height: 0; border-top: 1px solid var(--rule); }
  .fact-icon { position: absolute; left: 72px; width: 80px; height: 80px; }
</style>
</head>
<body>
<div class="page">
  <div class="side-band-top"></div>
  <div class="side-band-icons"></div>

  <section class="intro">
    <h1 class="product-name">FaultLens™</h1>
    <p>The Office of Digital Openness (ODO) has been helping eliminate the digital accessibility divide since 2001. We have analyzed more than 51,000 websites and our reports, tools, and services help our clients ensure that their sites are accessible to everyone, regardless of any particular disability or impairment.</p>
    <p>Now, we’re offering our exclusive FaultLensTM report, custom-tailored to your website, to help your organization identify and rectify digital accessibility risks.</p>
    <p>FaultLens™ is the most cost-effective first step on your path to compliance.</p>
  </section>

  <h2 class="facts-title">Quick facts:</h2>

  <!-- money -->
  <svg class="fact-icon" style="top:438px" viewBox="0 0 80 80" aria-hidden="true">
    <g fill="none" stroke="#fff" stroke-width="4" stroke-linejoin="round">
      <path d="M8 46 L46 26 L72 46 L34 66 Z"/>
      <path d="M8 52 L34 72 L72 52"/>
    </g>
    <circle cx="40" cy="44" r="9" fill="#fff"/>
    <text x="40" y="49" text-anchor="middle" font-size="13" font-weight="700" fill="#2eae6b" font-family="Arial, sans-serif">$</text>
  </svg>
  <p class="fact" style="top:461px">Failure to comply with Web Content Accessibility Guidelines (WCAG) 2.1 Level A/AA could result in tens of thousands of dollars (per incident) in legal fees from pending lawsuits.</p>
  <div class="fact-rule" style="top:548px"></div>

  <!-- gavel -->
  <svg class="fact-icon" style="top:580px" viewBox="0 0 80 80" aria-hidden="true">
    <g fill="#fff">
      <rect x="30" y="10" width="16" height="34" rx="2" transform="rotate(45 38 27)"/>
      <rect x="36" y="30" width="8" height="36" rx="3" transform="rotate(-45 40 48)"/>
      <rect x="6" y="62" width="30" height="6" rx="1"/>
      <rect x="10" y="54" width="22" height="8" rx="2"/>
    </g>
  </svg>
  <p class="fact" style="top:588px">Last year the number of website accessibility lawsuits increased by<br>177% vs. 2017.</p>
  <div class="fact-rule" style="top:670px"></div>

  <!-- eye -->
  <svg class="fact-icon" style="top:682px" viewBox="0 0 80 80" aria-hidden="true">
    <path d="M6 40 Q40 6 74 40 Q40 74 6 40 Z" fill="none" stroke="#fff" stroke-width="5"/>
    <circle cx="40" cy="40" r="10" fill="#fff"/>
  </svg>
  <p class="fact" style="top:713px">In New York state alone, 1,564 lawsuits were filed alleging websites<br>were not accessible to the blind or visually impaired.</p>
  <div class="fact-rule" style="top:793px"></div>

  <!-- coins -->
  <svg class="fact-icon" style="top:805px" viewBox="0 0 80 80" aria-hidden="true">
    <g fill="#fff">
      <rect x="42" y="4" width="26" height="8" rx="4"/><rect x="42" y="14" width="26" height="8" rx="4"/><rect x="42" y="24" width="26" height="8" rx="4"/>
      <rect x="4" y="40" width="26" height="8" rx="4"/><rect x="4" y="50" width="26" height="8" rx="4"/><rect x="4" y="60" width="26" height="8" rx="4"/>
      <circle cx="54" cy="56" r="18"/>
    </g>
    <text x="54" y="63" text-anchor="middle" font-size="20" font-weight="700" fill="#2eae6b" font-family="Arial, sans-serif">$</text>
  </svg>
  <p class="fact" style="top:827px">The cost of making websites accessible ranges from several thousand dollars to a few million dollars, depending on the complexity of the site.</p>
  <div class="fact-rule" style="top:915px"></div>

  <!-- alert badge -->
  <svg class="fact-icon" style="top:935px" viewBox="0 0 80 80" aria-hidden="true">
    <path d="M40 4 L48 16 L62 10 L62 25 L76 30 L68 42 L76 54 L62 58 L62 72 L48 66 L40 78 L32 66 L18 72 L18 58 L4 54 L12 42 L4 30 L18 25 L18 10 L32 16 Z" fill="none" stroke="#fff" stroke-width="4" stroke-linejoin="round"/>
    <rect x="36" y="24" width="8" height="24" rx="2" fill="#fff"/>
    <circle cx="40" cy="56" r="4.5" fill="#fff"/>
  </svg>
  <p class="fact wide" style="top:933px">And while numerous big-name companies have been sued (Northwire News, Blaze Burger, Parcelo, Cocoa Ridge, Pixelvane, Tunebox, Kaito Motors, Linen &amp; Loft, Halden Street, Valumart, Dishdash, Green Crate, Medicor, Rollo Pizza, Streamlet, Stridewell, Kindred Match, Harbor Union Bank, Freshway, Bolt Hardware, and hundreds more), small businesses also face great risk.</p>
  <div class="fact-rule" style="top:1037px"></div>

  <!-- light bulb -->
  <svg class="fact-icon" style="top:1058px" viewBox="0 0 80 80" aria-hidden="true">
    <g stroke="#fff" stroke-width="4" stroke-linecap="round" fill="none">
      <line x1="40" y1="4" x2="40" y2="12"/><line x1="14" y1="14" x2="20" y2="20"/><line x1="66" y1="14" x2="60" y2="20"/>
      <line x1="4" y1="38" x2="12" y2="38"/><line x1="68" y1="38" x2="76" y2="38"/>
      <line x1="10" y1="58" x2="16" y2="54"/><line x1="70" y1="58" x2="64" y2="54"/>
      <path d="M30 58 Q30 50 25 44 Q20 36 26 27 Q40 12 54 27 Q60 36 55 44 Q50 50 50 58 Z"/>
      <line x1="31" y1="65" x2="49" y2="65"/><line x1="33" y1="72" x2="47" y2="72"/>
    </g>
  </svg>
  <p class="fact" style="top:1075px">Trying to meet WCAG guidelines without the advantage of FaultLens™ could result in a tremendous amount of wasted time, money and effort. Don’t go it alone.</p>
</div>
</body>
</html>
```